French Puns

Creation of a cover for a book on French plays on words.
The public is lovers of the French language
TITLE: The gentle phrases of Honoré Vasseline
SUB-TITLE: Witty words, wit of words
PUBLISHER (at the bottom of the page): Editions Plumeau
(See joined examples, previous books of the same author)
Size: 14 x 20.5 cm
Please note that the text on the cover is in French, not in English:
Fine phrases from Honoré Vasseline
Witty words, witty words (subtitle, smaller)
Plumeau Editions

```html
<!DOCTYPE html>
<html lang="fr">
<head>
<meta charset="utf-8">
<title>Les bons mots d’Honoré Vasseline</title>
<link rel="stylesheet" href="https://fonts.googleapis.com/css2?family=Playfair+Display:wght@400&family=Poppins:wght@400;600&display=swap">
<style>
  :root {
    --backdrop: #5a5a5a;
    --paper: #ffffff;
    --ink: #222222;
    --title-green: #0e6e58;
    --title-red: #b84040;
    --title-blue: #2a52b8;
    --art-sky: #bcd7f2;
    --art-sand: #f5e3b8;
  }
  html, body {
    margin: 0;
    padding: 0;
    width: 1200px;
    height: 2400px;
    overflow: hidden;
    background: var(--backdrop);
  }
  .cover {
    position: absolute;
    left: 50px;
    top: 394px;
    width: 1100px;
    height: 1611px;
    background: var(--paper);
    box-shadow: 18px 22px 40px rgba(0, 0, 0, 0.45);
    overflow: hidden;
  }
  .title-line {
    position: absolute;
    left: 98px;
    margin: 0;
    font-family: "Playfair Display", Georgia, serif;
    font-weight: 400;
    font-size: 180px;
    line-height: 1;
    letter-spacing: -0.045em;
    white-space: nowrap;
  }
  .title-les { top: 159px; color: var(--title-green); }
  .title-bons { top: 307px; color: var(--title-red); letter-spacing: -0.07em; }
  .title-mots { top: 459px; color: var(--title-blue); }
  .title-author {
    font-size: 140px;
    color: var(--ink);
  }
  .title-author-first { top: 672px; }
  .title-author-last { top: 822px; }
  .subtitle {
    position: absolute;
    left: 98px;
    margin: 0;
    font-family: "Poppins", Arial, sans-serif;
    font-weight: 600;
    font-size: 66px;
    line-height: 1;
    color: var(--ink);
    white-space: nowrap;
  }
  .subtitle-first { top: 1179px; }
  .subtitle-second { top: 1265px; }
  .publisher {
    position: absolute;
    left: 98px;
    top: 1415px;
    margin: 0;
    font-family: "Poppins", Arial, sans-serif;
    font-weight: 400;
    font-size: 38px;
    line-height: 1;
    letter-spacing: 0.1em;
    color: var(--ink);
    white-space: nowrap;
  }
  .circus-art {
    position: absolute;
    border-radius: 46% 54% 42% 58% / 52% 44% 56% 48%;
    background: linear-gradient(180deg, var(--art-sky) 0%, var(--art-sky) 62%, var(--art-sand) 100%);
  }
  .art-hoop-dancer { left: 552px; top: 51px; width: 292px; height: 361px; }
  .art-aerial-hoop { left: 670px; top: 387px; width: 352px; height: 324px; background: var(--art-sky); }
  .art-juggler { left: 673px; top: 749px; width: 253px; height: 393px; }
  .art-clown { left: 768px; top: 1136px; width: 247px; height: 323px; }
</style>
</head>
<body>
  <main class="cover">
    <h1 class="book-title">
      <span class="title-line title-les">Les</span>
      <span class="title-line title-bons">bons</span>
      <span class="title-line title-mots">mots</span>
      <span class="title-line title-author title-author-first">d’Honoré</span>
      <span class="title-line title-author title-author-last">Vasseline</span>
    </h1>

    <div class="circus-art art-hoop-dancer" role="img" aria-label="Illustration d’une danseuse de cirque en tutu rouge jonglant avec des cerceaux"></div>
    <div class="circus-art art-aerial-hoop" role="img" aria-label="Illustration d’une acrobate suspendue dans un cerceau aérien"></div>
    <div class="circus-art art-juggler" role="img" aria-label="Illustration d’un jongleur sur un monocycle lançant des quilles"></div>
    <div class="circus-art art-clown" role="img" aria-label="Illustration d’un clown en pantalon rayé et chapeau à pois"></div>

    <h2 class="subtitle-block">
      <span class="subtitle subtitle-first">Mots d'esprit,</span>
      <span class="subtitle subtitle-second">esprit des mots</span>
    </h2>

    <p class="publisher">Éditions Plumeau</p>
  </main>
</body>
</html>
```